Calderwyn Structural Roof Inc.

We need a business card design for a commercial roofing company metro Boston based. We are a roofing company that help people manage buildings and build relationships with clients. We would like a unique card that stands out. We want a business card with a white background. We do not want a roof as the logo.

Industry/Entity Type

Roofing

```html
<!DOCTYPE html>
<html lang="en">
<head>
<meta charset="utf-8">
<title>Calderwyn Structural Roof Inc. — Business Card</title>
<link href="https://fonts.googleapis.com/css2?family=Oswald:wght@400;500&display=swap" rel="stylesheet">
<style>
  :root {
    --canvas: #c9c9c9;
    --paper: #ffffff;
    --ink: #000000;
    --brand-blue: #3a70b8;
    --faint: #ececec;
  }
  * { margin: 0; padding: 0; box-sizing: border-box; }
  html, body {
    width: 1065px; height: 1200px; overflow: hidden;
    background: var(--canvas);
    font-family: "Oswald", "Arial Narrow", sans-serif;
  }
  .card {
    position: absolute; left: 16px; width: 1040px; height: 576px;
    overflow: hidden;
  }
  .card svg.decor { position: absolute; inset: 0; }

  /* Front */
  .card--front { top: 13px; background: var(--paper); }
  .front-mark { position: absolute; left: 632px; top: 128px; }
  .front-name {
    position: absolute; right: 56px; top: 370px; text-align: right;
    color: var(--ink); font-weight: 500; font-size: 54px; line-height: 62px;
    text-transform: uppercase; letter-spacing: 0.5px;
  }

  /* Back */
  .card--back { top: 611px; background: var(--ink); color: var(--paper); }
  .holder { position: absolute; left: 42px; top: 52px; }
  .holder-name { font-size: 46px; font-weight: 400; line-height: 1.1; text-transform: uppercase; }
  .holder-title { color: var(--brand-blue); font-size: 42px; font-weight: 500; margin-left: 50px; line-height: 1.1; }
  .contact { position: absolute; left: 42px; top: 212px; font-size: 27px; line-height: 36px; text-transform: uppercase; }
  .contact .web { margin-top: 22px; }
  .address {
    position: absolute; left: 42px; top: 440px; color: var(--brand-blue);
    font-size: 33px; line-height: 44px; text-transform: uppercase;
  }
  .back-mark { position: absolute; left: 762px; top: 278px; }
  .back-name {
    position: absolute; left: 660px; top: 450px; width: 340px; text-align: center;
    color: var(--paper); font-weight: 500; font-size: 32px; line-height: 40px;
    text-transform: uppercase;
  }
</style>
</head>
<body>
  <section class="card card--front">
    <svg class="decor" width="1040" height="576" aria-hidden="true">
      <circle cx="200" cy="300" r="270" fill="none" stroke="var(--faint)" stroke-width="40"/>
    </svg>
    <svg class="front-mark" width="220" height="220" aria-hidden="true">
      <circle cx="110" cy="110" r="92" fill="none" stroke="var(--ink)" stroke-width="22"/>
    </svg>
    <h1 class="front-name">Calderwyn<br>Structural Roof Inc.</h1>
  </section>

  <section class="card card--back">
    <svg class="decor" width="1040" height="576" aria-hidden="true">
      <circle cx="1160" cy="770" r="620" fill="none" stroke="var(--paper)" stroke-width="40"/>
      <circle cx="1160" cy="770" r="585" fill="none" stroke="var(--brand-blue)" stroke-width="9"/>
    </svg>
    <div class="holder">
      <p class="holder-name">Marco Delvane</p>
      <p class="holder-title">President</p>
    </div>
    <div class="contact">
      <p>marco@calderwynroof.com</p>
      <p>Direct 781-555-0148</p>
      <p class="web">www.calderwynroof.com</p>
    </div>
    <div class="address">
      <p>88 Millbrook Ave.</p>
      <p>Stoneham , MA. 02180-1120</p>
    </div>
    <svg class="back-mark" width="140" height="140" aria-hidden="true">
      <circle cx="70" cy="70" r="52" fill="none" stroke="var(--paper)" stroke-width="12"/>
    </svg>
    <p class="back-name">Calderwyn<br>Structural Roof Inc.</p>
  </section>
</body>
</html>
```